Invitation - Photos with Santa

We’re doing an event this Christmas for people get photos with Santa.
It’ll be a postcard that we mail to people we know.
Size: 5 x 7, two sided
Details for back of postcard:
Saturday, December 4
10 a.m. - 12 p.m.
47315 Olvey Ln.
Strongsville, OH 44149
The company putting it on is Brindlecrest. I’ve got a million logo formats so just let me know what you need.
In terms of theme/look/feel for the front of card, I’m a little stuck so I’m open to whatever.
-Skip the line?
-Private Santa party?
-Screw the mall?
Attached is an old one we used last time time we did it.
Let me know if there are any questions!
People I know personally, people with kids, people who private photo with Santa without having to go to the mall

```html
<!DOCTYPE html>
<html lang="en">
<head>
<meta charset="utf-8">
<title>Brindlecrest – Photos with Santa Postcard</title>
<link rel="stylesheet" href="https://fonts.googleapis.com/css2?family=Open+Sans:wght@300;400;600&family=Great+Vibes&display=swap">
<style>
  :root {
    --backdrop: #bcbdbf;
    --navy: #2c3244;
    --navy-light: #4a5064;
    --coral: #ef7a5e;
    --cream: #e8e6d3;
    --paper: #ffffff;
    --ink: #2f3550;
    --rule: #9a9a9a;
  }
  * { margin: 0; padding: 0; box-sizing: border-box; }
  html, body { width: 924px; height: 1200px; overflow: hidden; }
  body { background: var(--backdrop); font-family: "Open Sans", Arial, sans-serif; position: relative; }

  .postcard { position: absolute; left: 120px; width: 672px; height: 480px; overflow: hidden; }
  .postcard--front { top: 91px; background: radial-gradient(ellipse at 70% 40%, var(--navy-light) 0%, var(--navy) 65%); }
  .postcard--back { top: 627px; background: var(--paper); }

  /* front */
  .photo-stamp {
    position: absolute; left: 29px; top: 24px; width: 317px; height: 432px;
    transform: rotate(-4deg); background: var(--cream); padding: 12px;
  }
  .photo-stamp__image {
    width: 100%; height: 100%;
    background: linear-gradient(160deg, #6b5040 0%, #8a2a25 40%, #d9cbb5 65%, #7a3a2c 100%);
  }
  .greeting-lettering {
    position: absolute; left: 370px; top: 26px; width: 268px; height: 272px;
    background: radial-gradient(ellipse at center, rgba(239,122,94,0.35) 0%, rgba(239,122,94,0.08) 70%, rgba(239,122,94,0) 100%);
  }
  .tagline {
    position: absolute; left: 372px; top: 314px; width: 286px; height: 48px;
    border-top: 3px double var(--coral); border-bottom: 3px double var(--coral);
    color: var(--cream); font-size: 27px; font-weight: 400; letter-spacing: 1px;
    text-align: center; line-height: 42px;
  }
  .brand {
    position: absolute; display: flex; align-items: center; gap: 6px;
    color: var(--coral); font-weight: 600; font-size: 15px;
  }
  .brand__dot { width: 10px; height: 10px; border-radius: 50%; background: var(--coral); }
  .brand--front { left: 462px; top: 406px; }
  .brand--back { left: 372px; top: 58px; }

  /* back */
  .invite { position: absolute; left: 24px; top: 24px; width: 300px; text-align: center; }
  .invite__host { color: var(--ink); font-size: 19px; font-weight: 600; line-height: 25px; }
  .invite__details { margin-top: 9px; color: var(--coral); font-size: 22px; font-weight: 300; line-height: 28px; }
  .invite__for { margin-top: 4px; color: var(--coral); font-family: "Great Vibes", cursive; font-size: 36px; line-height: 36px; }
  .invite__event {
    margin: 2px auto 0; width: 244px; border-top: 1px solid var(--coral); border-bottom: 1px solid var(--coral);
    color: var(--ink); font-size: 22px; line-height: 34px;
  }
  .invite__address { margin-top: 11px; color: var(--coral); font-size: 13.5px; font-weight: 300; }
  .invite__note { margin-top: 12px; color: var(--ink); font-size: 17px; line-height: 21px; }
  .closing-lettering {
    position: absolute; left: 24px; top: 374px; width: 298px; height: 90px;
    background: radial-gradient(ellipse at center, rgba(239,122,94,0.3) 0%, rgba(239,122,94,0) 75%);
  }
  .divider { position: absolute; left: 344px; top: 24px; width: 1px; height: 418px; background: var(--rule); }
</style>
</head>
<body>
  <section class="postcard postcard--front">
    <div class="photo-stamp">
      <div class="photo-stamp__image" role="img" aria-label="Photo of Santa in a festive room with a Christmas tree and a toddler running from him"></div>
    </div>
    <div class="greeting-lettering" role="img" aria-label="Hand-lettered Peace and Joy with a hanging ornament"></div>
    <p class="tagline">SCREW THE MALL</p>
    <div class="brand brand--front"><span class="brand__dot"></span>Brindlecrest</div>
  </section>

  <section class="postcard postcard--back">
    <div class="invite">
      <p class="invite__host">THE BRINDLECREST TEAM<br>INVITES YOU TO</p>
      <p class="invite__details">JOIN US<br>Saturday, December 4<br>10 a.m. - 12 p.m.</p>
      <p class="invite__for">for</p>
      <p class="invite__event">PHOTOS WITH SANTA</p>
      <p class="invite__address">47315 Olvey Ln. Strongsville, OH 44149</p>
      <p class="invite__note">Prepare to skip the lines<br>and capture memorable photos<br>for the holiday season</p>
    </div>
    <div class="closing-lettering" role="img" aria-label="Hand-lettered Peace and Joy with a hanging ornament"></div>
    <div class="divider"></div>
    <div class="brand brand--back"><span class="brand__dot"></span>Brindlecrest</div>
  </section>
</body>
</html>
```